The task involves the design and creation of a wordpress website for plainpacts.co.
Plainpacts.co is a website through which people can purchase template legal contracts.The website is focused on Australian users although in the future we may target users in other countries.
*************************************************
We will offer 3 bundles of products (a small business, medium business and a large business bundle) as follows:
(a) a Starter package ($199);
(b) a Pro (professional) package ($499);
(c) an Enterprise package ($1,500).
Each bundle contains a number of legal templates. The Pro package includes all of the legal templates in the Starter package. The Enterprise version contains all the legal templates in the Starter and Pro package.
The starter bundle will include the following legal documents:
+Website terms and conditions
+Confidentiality agreement
+Services agreement
+Purchase order terms and conditions
+Variation agreement
+Independent contractor agreement
+Term sheet
The Pro bundle includes:
+ all of the documents contained in the Starter package plus
+ Request for tender
+ Consultancy agreement
+ Contract labour agreement
+ Sponsorship agreement
The Enterprise package includes:
+All of the documents in our Pro package plus
+Freight Services agreement
+IT Services agreement
+Website design and hosting agreement
+Teaming agreement
+Long form services agreement
+Distribution agreement
+Content supply agreement
****************************************************
We like the simplicity and layout of the following websites:
http://leavewatcher.com/
https://www.trymeadow.com/
http://www.helpquarry.com/
http://www.nodlegal.com/
http://usebrindle.com/
We like the way on the leavewatcher.com page when you click on the pricing tab and other tabs of the navigation bar you are taken lower down on the homepage to the content. We like the static header on leavewatcher and Helpquarry. We also like the use of big headings, images and symbols to convey meaning as well as having the webpage broken into sections.
We will want an email sign up capability and will need to integrate an email collection capability with postwren or similar.
We like the way it is referred to on the https://www.harbordocs.com/ website where it says:
"Your first document is free" and them there is an email sign up box.
We imagine having a similar features at a couple of places on the site with a call to action.
We also imagine including some sort of website abandonment application similar to http://leavewatcher.com/ or http://pagetrellis.com/. We would also like a countdown clock linked to a discount off the price of the bundles. Please provide a recommendation and ensure that this can easily be integrated.
We will need an e-commence capability so that we can sell our products.
******************************************
Our value proposition is as follows:
1. Lower your legal costs by using our template documents as a starting point
Why pay a lawyer to create a document from scratch when you can you our template agreements as the starting point.
2. Variety of bundles to chose from
We offer you the opportunity to purchase the bundle of documents that are just right for you – small business, medium business and large business options.
3.Customise agreements yourself or have your lawyer customise them for you.
Our contracts are drafted in plain English and you can provide them to your lawyer and ask them to customise them for you.
4. Reviewed by top lawyers - customised for Australia
All of our legal documents have been reviewed by a lawyer with experience working at a top international law firm.
***************************************************
The benefits of the service are:
* Documents reviewed by Australian lawyer with experience at top tier Australian law firm.
* Cost effective approach to risk management
* Electronic delivery
* Use templates as often as you like for your internal business purposes
* Free explanation of each template agreement
* Sensible approach to legal drafting to minimise contract negotiation time
*****************************************************
We will need to include the following across the bottom of each webpage.
"Copyright 2014 PlainPacts. All rights reserved. PlainPacts provides information only. PlainPacts is not a "lawyer referral service" and does not provide legal advice or participate in any legal representation. PlainPacts is not a law firm or a substitute for a qualified lawyer or law firm. For legal advice, please contact a lawyer. Use of PlainPacts.co is subject to our Terms and Conditions."
The reference to Terms and Conditions will be a link to the Terms and Conditions.
*********************************************************
The Contact Us section should be a simple webform. We will not include any telephone or physical address at this stage.
For the About Us section
We can include the following:
PlainPacts was conceived and nurtured in Melbourne, the world's most liveable city by an experienced lawyer who loves the idea of making legal contracting affordable for small and medium size businesses. We have friends in other cities who help make PlainPacts possible.
************************************************************
We expect the website created to be user friendly, able to be updated easily, optimised for search engines and to be built on wordpress. The website should be able to integrate with third party applications (eg analytic software, email marketing tools etc). Please include recommendations for third party software for integration. We have installed Wordpress 3.9.
Target Market(s)
Small to medium business owners.

```html
<!DOCTYPE html>
<html lang="en">
<head>
<meta charset="utf-8">
<title>PlainPacts.co — Template legal contracts</title>
<link rel="stylesheet" href="https://fonts.googleapis.com/css2?family=Arvo:wght@400;700&display=swap">
<style>
  :root {
    --teal: #0ab4c6;
    --teal-dark: #079fb0;
    --white: #ffffff;
    --ink: #333333;
    --nav-active: #3c9aa6;
    --page-grey: #f3f3f3;
    --rule: #cfd3d6;
    --box-border: #c9c9c9;
    --overlay: rgba(20, 18, 16, 0.55);
  }
  * { box-sizing: border-box; margin: 0; padding: 0; }
  html, body {
    width: 1200px; height: 809px; overflow: hidden;
    font-family: "Arvo", Georgia, serif;
    background: var(--page-grey);
    color: var(--ink);
  }
  .site { position: relative; width: 1200px; height: 809px; }

  .utility-bar {
    height: 48px; background: var(--teal); color: var(--white);
    display: flex; align-items: center; justify-content: space-between;
    padding: 0 33px 0 43px; font-size: 16px;
  }
  .cart-summary { display: flex; align-items: center; gap: 8px; }
  .account-links { display: flex; gap: 22px; font-size: 15px; }
  .account-links a { color: var(--white); text-decoration: none; }

  .main-header {
    height: 85px; background: var(--white);
    display: flex; align-items: center; justify-content: space-between;
    padding: 0 22px 0 43px;
  }
  .brand {
    font-size: 32px; color: var(--teal); letter-spacing: -0.5px;
    text-decoration: none; font-weight: 400;
  }
  .main-nav { display: flex; gap: 34px; font-size: 16px; }
  .main-nav a { color: var(--ink); text-decoration: none; }
  .main-nav a.is-current { color: var(--nav-active); }

  .hero {
    position: relative; height: 534px; overflow: hidden;
  }
  .hero-photo {
    position: absolute; inset: 0;
    background:
      linear-gradient(90deg, rgba(0,0,0,0) 0%, rgba(0,0,0,0) 48%, rgba(30,32,38,0.85) 60%, rgba(40,44,52,0.9) 78%, rgba(120,112,100,0.6) 100%),
      linear-gradient(180deg, #7a5a34 0%, #c69b5a 35%, #8b5e2e 60%, #3a2a1c 100%);
  }
  .hero-title {
    position: absolute; left: 43px; top: 142px;
    width: 381px; height: 68px; background: var(--overlay);
    color: var(--white); font-size: 35px; font-weight: 400;
    display: flex; align-items: center; padding-left: 15px;
  }
  .hero-lede {
    position: absolute; left: 43px; top: 234px;
    width: 1047px; height: 52px; background: var(--overlay);
    color: var(--white); font-size: 19.5px;
    display: flex; align-items: center; padding-left: 25px;
  }
  .hero-cta {
    position: absolute; left: 43px; top: 304px;
    width: 297px; height: 57px; border-radius: 4px;
    background: linear-gradient(180deg, var(--teal) 0%, var(--teal-dark) 100%);
    color: var(--white); font-size: 26px; text-decoration: none;
    display: flex; align-items: center; justify-content: center;
  }
  .slide-dots {
    position: absolute; top: 491px; left: 561px;
    display: flex; gap: 12px;
  }
  .slide-dots span {
    width: 18px; height: 18px; border-radius: 50%;
    background: #8a8a8a; display: block;
  }
  .slide-dots span.is-active { background: transparent; border: 3px solid #a9a9a9; }

  .packages { border-top: 5px solid var(--rule); padding: 51px 0 0 43px; }
  .package-tab {
    display: inline-flex; align-items: center; justify-content: center;
    width: 216px; height: 56px; border: 1px solid var(--box-border);
    background: #f7f7f7; font-size: 17px; color: #444;
  }
</style>
</head>
<body>
<div class="site">
  <div class="utility-bar">
    <div class="cart-summary">
      <svg width="24" height="18" viewBox="0 0 24 18" aria-hidden="true">
        <path d="M1 2h4l3 10h11l3-8H7" fill="none" stroke="#fff" stroke-width="2" stroke-linejoin="round"/>
        <circle cx="10" cy="15.5" r="1.8" fill="#fff"/><circle cx="18" cy="15.5" r="1.8" fill="#fff"/>
      </svg>
      <span>0 items - ( $0 in total )</span>
    </div>
    <nav class="account-links"><a href="#">Register</a><a href="#">Login</a></nav>
  </div>

  <header class="main-header">
    <a class="brand" href="#">PlainPacts.co</a>
    <nav class="main-nav">
      <a class="is-current" href="#">Home</a>
      <a href="#">About</a>
      <a href="#">Products</a>
      <a href="#">My Account</a>
      <a href="#">Contact</a>
    </nav>
  </header>

  <section class="hero">
    <div class="hero-photo" role="img" aria-label="Photo of a lawyer in a suit writing notes in an open law book, with blurred shelves of legal volumes behind"></div>
    <h1 class="hero-title">Enterprise package</h1>
    <p class="hero-lede">Built for big business, this package combines all our offerings to meet the needs of larger organisations</p>
    <a class="hero-cta" href="#">Buy Now</a>
    <div class="slide-dots"><span></span><span class="is-active"></span><span></span></div>
  </section>

  <section class="packages">
    <div class="package-tab">Document Package</div>
  </section>
</div>
</body>
</html>
```